Gobal construction supply company needs new business card design

I need a business card design for my global supply company using an existing logo. i will be looking to print these on rounded corner cards with the black background version of my logo on the back. on the front white background, my logo again and my simple details.

```html
<!DOCTYPE html>
<html lang="en">
<head>
<meta charset="utf-8">
<title>Meridian Build Supply – Business Cards</title>
<link rel="stylesheet" href="https://fonts.googleapis.com/css2?family=Montserrat:wght@700&family=Roboto:wght@400;500;700&display=swap">
<style>
  :root {
    --stage: #3c3c3e;
    --card-black: #111111;
    --card-white: #ffffff;
    --brand-red: #d90000;
    --ink: #111111;
    --ink-soft: #333333;
    --ring: #d6d6d6;
  }
  * { margin: 0; padding: 0; box-sizing: border-box; }
  html, body {
    width: 1200px; height: 1000px; overflow: hidden;
    background: var(--stage);
    font-family: "Roboto", Arial, sans-serif;
  }
  .card {
    position: absolute; left: 220px;
    width: 760px; height: 430px;
    border-radius: 26px; overflow: hidden;
  }
  .card--back { top: 40px; background: var(--card-black); }
  .card--front { top: 530px; background: var(--card-white); }

  .brand {
    position: absolute; left: 0; right: 0;
    display: flex; justify-content: center; align-items: center; gap: 14px;
  }
  .brand__name {
    font-family: "Montserrat", Arial, sans-serif;
    font-weight: 700; letter-spacing: 1px; text-transform: uppercase;
  }
  .brand__dot { width: 22px; height: 22px; border-radius: 50%; background: var(--brand-red); }

  .card--back .brand { top: 190px; }
  .card--back .brand__name { color: #ffffff; font-size: 38px; }

  .card--front .brand { top: 60px; }
  .card--front .brand__name { color: var(--ink); font-size: 30px; }
  .card--front .brand__dot { width: 18px; height: 18px; }

  .person { position: absolute; top: 130px; left: 0; right: 0; text-align: center; }
  .person__name { color: var(--brand-red); font-weight: 700; font-size: 26px; letter-spacing: 0.5px; text-transform: uppercase; }
  .person__title { color: var(--ink-soft); font-size: 15px; margin-top: 4px; }

  .contacts {
    position: absolute; top: 215px; left: 30px; right: 30px;
    display: flex; justify-content: space-between;
  }
  .contact { width: 170px; display: flex; flex-direction: column; align-items: center; gap: 8px; }
  .contact__icon {
    width: 46px; height: 46px; border-radius: 50%;
    background: var(--brand-red); border: 3px solid var(--ring);
    display: flex; align-items: center; justify-content: center;
  }
  .contact__icon svg { width: 22px; height: 22px; }
  .contact__text { color: var(--ink); font-weight: 500; font-size: 15px; white-space: nowrap; }
  .contact__text em { font-style: normal; color: var(--brand-red); }

  .rule { position: absolute; left: 0; right: 0; top: 330px; height: 6px; background: var(--ink); }
  .band {
    position: absolute; left: 0; right: 0; top: 342px; bottom: 0;
    background: var(--brand-red);
    display: flex; align-items: center; padding-left: 60px;
  }
  .band__address { color: #ffffff; font-weight: 500; font-size: 17px; letter-spacing: 0.3px; }
</style>
</head>
<body>

<section class="card card--back" aria-label="Card back">
  <div class="brand">
    <span class="brand__name">Meridian Build Supply</span>
    <span class="brand__dot"></span>
  </div>
</section>

<section class="card card--front" aria-label="Card front">
  <div class="brand">
    <span class="brand__name">Meridian Build Supply</span>
    <span class="brand__dot"></span>
  </div>

  <div class="person">
    <p class="person__name">Daniel Marsh</p>
    <p class="person__title">Managing Director</p>
  </div>

  <ul class="contacts">
    <li class="contact">
      <span class="contact__icon">
        <svg viewBox="0 0 24 24" fill="#fff"><path d="M6.6 10.8a15.1 15.1 0 0 0 6.6 6.6l2.2-2.2a1 1 0 0 1 1-.25 11.4 11.4 0 0 0 3.6.57 1 1 0 0 1 1 1V20a1 1 0 0 1-1 1A17 17 0 0 1 3 4a1 1 0 0 1 1-1h3.5a1 1 0 0 1 1 1c0 1.25.2 2.45.57 3.57a1 1 0 0 1-.25 1z"/></svg>
      </span>
      <span class="contact__text">+1 (555) 210 4478</span>
    </li>
    <li class="contact">
      <span class="contact__icon">
        <svg viewBox="0 0 24 24" fill="none" stroke="#fff" stroke-width="2"><rect x="7" y="2.5" width="10" height="19" rx="2"/><line x1="11" y1="18" x2="13" y2="18"/></svg>
      </span>
      <span class="contact__text">+1 (555) 210 4478</span>
    </li>
    <li class="contact">
      <span class="contact__icon">
        <svg viewBox="0 0 24 24" fill="none" stroke="#fff" stroke-width="2"><rect x="3" y="6" width="18" height="13" rx="1"/><polyline points="3,7 12,13 21,7"/></svg>
      </span>
      <span class="contact__text">dan@meridianbs.com</span>
    </li>
    <li class="contact">
      <span class="contact__icon">
        <svg viewBox="0 0 24 24" fill="none" stroke="#fff" stroke-width="1.8"><circle cx="12" cy="12" r="9"/><ellipse cx="12" cy="12" rx="4" ry="9"/><line x1="3" y1="12" x2="21" y2="12"/></svg>
      </span>
      <span class="contact__text">www.<em>meridianbs</em>.com</span>
    </li>
  </ul>

  <div class="rule"></div>
  <div class="band">
    <p class="band__address">4820 Harbor Avenue, Portside, NY 10451</p>
  </div>
</section>

</body>
</html>
```